AK MERIDEL BUSINESS CARD DESIGN PROJECT

We need to utilize our logo that was expertly created on Markvelloo and now need to match this with a business card design.

```html
<!DOCTYPE html>
<html lang="en">
<head>
<meta charset="UTF-8">
<title>AK Meridel Business Card</title>
<link href="https://fonts.googleapis.com/css2?family=Lato:wght@400;700;900&display=swap" rel="stylesheet">
<style>
  :root {
    --bg: #2b2b2b;
    --brand-blue: #0453a8;
    --ink-blue: #0b54b0;
    --card-white: #ffffff;
    --text-grey: #4a4a4a;
    --silver: #e6e8ea;
  }
  * { margin: 0; padding: 0; box-sizing: border-box; }
  html, body {
    width: 1200px; height: 875px; overflow: hidden;
    background: var(--bg);
    font-family: "Lato", sans-serif;
  }
  .canvas {
    position: relative; width: 1200px; height: 875px;
  }
  .card {
    position: absolute; top: 283px;
    width: 540px; height: 309px;
    border-radius: 22px;
    overflow: hidden;
  }
  .card-front { left: 40px; background: var(--brand-blue); }
  .card-back { left: 620px; background: var(--card-white); }

  .wordmark {
    display: flex; align-items: center; gap: 14px;
    font-family: "Lato", sans-serif; font-weight: 900;
    letter-spacing: 0.16em; white-space: nowrap;
  }
  .wordmark-mark { display: block; }
  .card-front .wordmark {
    position: absolute; left: 50%; top: 50%;
    transform: translate(-50%, -50%);
    font-size: 40px; color: var(--silver);
  }
  .card-front .wordmark-mark { width: 26px; height: 26px; background: var(--silver); }

  .card-back .wordmark {
    position: absolute; left: 30px; top: 180px;
    font-size: 25px; color: var(--ink-blue); gap: 10px;
  }
  .card-back .wordmark-mark { width: 16px; height: 16px; background: var(--ink-blue); }

  .divider {
    position: absolute; left: 292px; top: 38px;
    width: 8px; height: 234px;
  }

  .contact {
    position: absolute; left: 318px; top: 40px;
    color: var(--text-grey);
  }
  .contact-name {
    font-weight: 900; font-size: 20px; color: var(--ink-blue);
    letter-spacing: 0.01em;
  }
  .contact-title { font-size: 14px; margin-top: 2px; }
  .contact-address { font-size: 13px; line-height: 1.4; margin-top: 12px; }
  .contact-list { list-style: none; margin-top: 12px; }
  .contact-list li {
    display: flex; align-items: center; gap: 9px;
    font-size: 13px; line-height: 21px;
  }
  .contact-list svg { width: 11px; height: 11px; fill: var(--ink-blue); flex: none; }
</style>
</head>
<body>
<div class="canvas">

  <section class="card card-front" aria-label="Card front">
    <div class="wordmark"><span class="wordmark-mark"></span>AK MERIDEL</div>
  </section>

  <section class="card card-back" aria-label="Card back">
    <div class="wordmark"><span class="wordmark-mark"></span>AK MERIDEL</div>

    <svg class="divider" viewBox="0 0 8 234" aria-hidden="true">
      <path d="M0 0 L5 0 L5 44 L4 48 L2.6 48 L2.6 234 L1.6 234 L1.6 48 L0 44 Z" fill="#0b54b0"/>
    </svg>

    <div class="contact">
      <div class="contact-name">DANIEL REYES</div>
      <div class="contact-title">Founder &amp; CEO</div>
      <div class="contact-address">123 Anywhere St.<br>Any City, ST 12345</div>
      <ul class="contact-list">
        <li><svg viewBox="0 0 12 12"><path d="M2.5 0.5l2 2.5-1.2 1.3c.7 1.6 2 2.9 3.6 3.6l1.3-1.2 2.5 2-1.2 2.3C4.8 10.8 1.2 7.2.2 1.7z"/></svg>(123) 456-7890</li>
        <li><svg viewBox="0 0 12 12"><path d="M3 0h6v12H3zM4 1.5v8h4v-8z"/></svg>(231) 456-7890</li>
        <li><svg viewBox="0 0 12 12"><path d="M3 0h6v3H3zM0 4h12v5h-2v3H2V9H0zM3 8v3h6V8z"/></svg>(312) 456-7890</li>
        <li><svg viewBox="0 0 12 12"><path d="M0 2h12v1L6 7 0 3zM0 4.5l6 4 6-4V10H0z"/></svg>hello@akmeridel.com</li>
        <li><svg viewBox="0 0 12 12"><path d="M6 0a6 6 0 1 0 0 12A6 6 0 0 0 6 0zm0 1.2a4.8 4.8 0 0 1 0 9.6 4.8 4.8 0 0 1 0-9.6zM5.4 1.4v9.2h1.2V1.4zM1.3 5.4v1.2h9.4V5.4z"/></svg>www.akmeridel.com</li>
      </ul>
    </div>
  </section>

</div>
</body>
</html>
```